Innovative label design for premium vodka bottle

We are looking for a bottle design (with logo) for a new premium vodka company based in Uganda. We are the first company to produce a premium vodka in Uganda made exclusively with local ingredients. We want the label design to set us apart from the more traditional (read boring) designs of local packaging and bring raise the bar for Ugandan packaging design.

We will initially sell to local markets and hope to go global in two years. The vodka is called "IRONCREST" after the famous adult mountain gorillas which live in the mountains of western Uganda.

The bottle design has to be simple and appealing to both an Africana and an International consumer (tourists). Simple, clean and to the point. The main color should be green and can or cannot include a rendering of a gorilla. Silver must also be included in the design (could be printed on metallic paper). It also can include the mountain landscapes of western Uganda. But please we are also open to more creative ideas which stray from these typical images of Uganda. I will attach some images of the silverback, the mountains of Uganda and other labels of local alcoholic beverages. Must be printed on paper. Can be glossy, matte or metallic. Do not submit ideas for labels printing on transparent film.

The size of the label should be 75mm wide by 120mm high. Also attached is an image of the bottle to be used.

Text that MUST be on the label:

Ironcrest
Ultra-Premium Vodka
Produced in Uganda
Triple Distilled from Sugar Cane
42.5%ABV
700ML

Text that CAN be incorporated:
Purely Ugandan
Triple Distilled-Ten Times filtered
3X Distilled - 10X Filtered

Please feel free to contact me with any inquiries.
Updates

Project Deadline Extended
Reason: Since we cannot meet until Wednesday to consider the designs, may as well allow the crowd a couple more days of creativity. Cheers, Bram

Hi,

Thank you all for your updates. We are currently ging through the designs and hope to have a decision made by the end of the week.

Well done!

Cheers,

Bram

Target Market(s)

Upmarket Ugandans and International consumers

Industry/Entity Type

Adult

Requirements
Must have
• Must be printed on paper. Can be glossy, matte or metallic. Do not submit ideas for labels printing on transparent film.

```html
<!DOCTYPE html>
<html lang="en">
<head>
<meta charset="utf-8">
<title>Ironcrest Ultra-Premium Vodka – Label</title>
<link rel="stylesheet" href="https://fonts.googleapis.com/css2?family=Tinos:wght@400;700&display=swap">
<style>
  :root {
    --stage-top: #ffffff;
    --stage-bottom: #e2e2e2;
    --label-grey: #dedede;
    --panel-white: #ffffff;
    --silver: #b9b9bd;
    --forest: #2e5b3d;
    --lime: #9ccd2f;
    --lime-deep: #6fae22;
    --band-dark: #3f8f2a;
    --band-light: #8cc63f;
    --vodka-red: #e0393e;
    --ink: #222222;
    --sky: #8fb3d6;
    --hill: #4d6b5a;
  }
  html, body {
    margin: 0;
    padding: 0;
    width: 1200px;
    height: 999px;
    overflow: hidden;
  }
  body {
    background: linear-gradient(180deg, var(--stage-top), var(--stage-bottom));
    font-family: "Tinos", "Times New Roman", serif;
  }
  .label {
    position: absolute;
    left: 390px;
    top: 130px;
    width: 420px;
    height: 560px;
  }
  .label__shape {
    position: absolute;
    inset: 0;
  }
  .label__scenery {
    position: absolute;
    left: 140px;
    top: 102px;
    width: 140px;
    height: 76px;
    border-radius: 50%;
    background: linear-gradient(180deg, #dfe9f3 0%, var(--sky) 45%, var(--hill) 100%);
    border: 2px solid var(--lime-deep);
  }
  .label__scrollwork {
    position: absolute;
    border-radius: 40px;
    background: radial-gradient(ellipse at center, rgba(156,205,47,0.22), rgba(156,205,47,0) 70%);
  }
  .label__scrollwork--crown { left: 70px; top: 70px; width: 280px; height: 130px; }
  .label__scrollwork--under { left: 140px; top: 262px; width: 140px; height: 36px; }
  .label__brand {
    position: absolute;
    left: 0;
    right: 0;
    top: 214px;
    text-align: center;
    font-weight: 700;
    font-size: 46px;
    letter-spacing: 1px;
    color: var(--lime);
    line-height: 1;
  }
  .label__divider {
    position: absolute;
    left: 70px;
    width: 280px;
    height: 2px;
    background: linear-gradient(90deg, rgba(156,205,47,0), var(--lime), rgba(156,205,47,0));
  }
  .label__divider--top { top: 306px; }
  .label__divider--bottom { top: 448px; }
  .label__text {
    position: absolute;
    left: 0;
    right: 0;
    text-align: center;
    margin: 0;
    line-height: 1;
  }
  .label__category { top: 320px; font-size: 22px; color: var(--vodka-red); letter-spacing: 0.5px; }
  .label__origin { top: 354px; font-size: 17px; color: var(--ink); }
  .label__process { top: 388px; font-size: 17px; color: var(--lime-deep); }
  .label__volume { top: 423px; font-size: 11px; color: var(--ink); }

  .neck-band {
    position: absolute;
    left: 390px;
    top: 702px;
    width: 420px;
    height: 70px;
    background: linear-gradient(90deg, var(--band-dark), var(--band-light) 50%, var(--band-dark));
    color: #ffffff;
    text-align: center;
  }
  .neck-band__line {
    margin: 0;
    position: absolute;
    left: 0;
    right: 0;
    line-height: 1;
  }
  .neck-band__line--main { top: 12px; font-size: 11px; }
  .neck-band__line--sub { top: 30px; font-size: 10px; }
  .neck-band__rule {
    position: absolute;
    left: 110px;
    right: 110px;
    top: 52px;
    height: 1px;
    background: rgba(255,255,255,0.75);
  }
</style>
</head>
<body>
  <main class="label">
    <svg class="label__shape" viewBox="0 0 420 560" width="420" height="560" aria-hidden="true">
      <defs>
        <linearGradient id="ground" x1="0" y1="0" x2="0" y2="1">
          <stop offset="0" stop-color="#e6e6e6"/>
          <stop offset="1" stop-color="#d6d6d6"/>
        </linearGradient>
        <radialGradient id="seal" cx="0.4" cy="0.35" r="0.7">
          <stop offset="0" stop-color="#c6ec6a"/>
          <stop offset="1" stop-color="#5ea21f"/>
        </radialGradient>
      </defs>
      <rect x="0" y="0" width="420" height="560" fill="url(#ground)"/>
      <path d="M0 178 C40 62 130 22 210 22 C290 22 380 62 420 178" fill="none" stroke="#2e5b3d" stroke-width="20"/>
      <path d="M8 186 C48 76 134 40 210 40 C286 40 372 76 412 186" fill="none" stroke="#9ccd2f" stroke-width="12"/>
      <path d="M18 190 C18 86 110 46 210 46 C310 46 402 86 402 190 V500 Q402 515 387 515 H230 L210 536 L190 515 H33 Q18 515 18 500 Z"
            fill="#ffffff" stroke="#b9b9bd" stroke-width="3"/>
      <circle cx="210" cy="22" r="17" fill="#ffffff" stroke="#b9b9bd" stroke-width="2"/>
      <circle cx="210" cy="22" r="12" fill="url(#seal)"/>
      <g fill="#9ccd2f">
        <polygon points="78,205 81,213 89,213 83,218 85,226 78,221 71,226 73,218 67,213 75,213"/>
        <polygon points="342,205 345,213 353,213 347,218 349,226 342,221 335,226 337,218 331,213 339,213"/>
      </g>
    </svg>

    <div class="label__scrollwork label__scrollwork--crown" role="img" aria-label="Green ornamental scrollwork framing the landscape"></div>
    <div class="label__scenery" role="img" aria-label="Oval photograph of misty green mountains of western Uganda"></div>

    <h1 class="label__brand">IRONCREST</h1>
    <div class="label__scrollwork label__scrollwork--under" role="img" aria-label="Silver ornamental flourish beneath the name"></div>

    <div class="label__divider label__divider--top"></div>
    <p class="label__text label__category">ULTRA-PREMIUM VODKA</p>
    <p class="label__text label__origin">Produced in Uganda</p>
    <p class="label__text label__process">Triple Distilled from Sugar Cane</p>
    <p class="label__text label__volume">42.5%ABV, 700ML</p>
    <div class="label__divider label__divider--bottom"></div>
  </main>

  <section class="neck-band">
    <p class="neck-band__line neck-band__line--main">★ &nbsp;Purely Ugandan, Triple Distilled-Ten Times filtered&nbsp; ★</p>
    <p class="neck-band__line neck-band__line--sub">3X Distilled - 10X Filtered</p>
    <div class="neck-band__rule"></div>
  </section>
</body>
</html>
```